Ridgeline Outfitters Business Cards

Recently had a logo done with Artfolio and now looking for a business card to go along with it.

Target Market(s)

Ridgeline Outfitters is a weapons dealer. My market will be primarily men, hunting, shooting type.

Industry/Entity Type

Business

Contact Information for Business Card

I selected double sided, but this is not required, single or double is going to be fine. I picture the logo on one side, or perhaps just the circle which contains "RO" with the remaining info on the other side.

Font styles to use
Sans Serif

Requirements
Must have
• My name: Milo Brandt
• Title: Owner
• tel: 612-555-0187
• web: www.ridgelineoutfittersmn.example
Nice to have
• I like the concept of a black business card. I would like to keep the colors monotone, black, grey, white or red. Red is acceptable because it is in the logo. I have also seen cards that are matte black with shiny black as well, perhaps for the logo (or circle RO) part of the logo.
• I will upload a couple of the logos for use, and also an example I just found of the black on black. and some others that have a nice contrast.
Should not have
• lots of colors are not wanted.

```html
<!DOCTYPE html>
<html lang="en">
<head>
<meta charset="utf-8">
<title>Ridgeline Outfitters Business Cards</title>
<link href="https://fonts.googleapis.com/css2?family=Jost:wght@400;500;700&display=swap" rel="stylesheet">
<style>
  :root {
    --page: #ffffff;
    --card: #000000;
    --red: #e31b23;
    --grey: #4d4d4d;
    --white: #ffffff;
  }
  * { margin: 0; padding: 0; box-sizing: border-box; }
  html, body {
    width: 1200px; height: 1000px; overflow: hidden;
    background: var(--page);
    font-family: "Jost", "Futura", sans-serif;
  }
  .canvas { position: relative; width: 1200px; height: 1000px; }
  .card {
    position: absolute; left: 326px; width: 548px; height: 315px;
    background: var(--card);
  }
  .card--front { top: 135px; }
  .card--back { top: 550px; }

  .brand {
    position: absolute; left: 404px; top: 242px;
    display: flex; align-items: center; gap: 26px;
  }
  .brand__ring { width: 100px; height: 100px; display: block; }
  .brand__name {
    color: var(--red); font-weight: 700; font-size: 26px;
    letter-spacing: 0.5px; text-transform: uppercase; white-space: nowrap;
  }

  .emblem {
    position: absolute; left: 382px; top: 629px; width: 156px; height: 156px;
    display: flex; align-items: center; justify-content: center;
  }
  .emblem svg { position: absolute; inset: 0; }
  .emblem__name {
    position: relative; color: var(--red); font-weight: 700; font-size: 15px;
    text-transform: uppercase; text-align: center; line-height: 1.25;
  }

  .divider {
    position: absolute; left: 575px; top: 572px; width: 1px; height: 273px;
    background: var(--white);
  }
  .contact { position: absolute; left: 610px; top: 660px; color: var(--white); }
  .contact__name { font-size: 21px; font-weight: 500; line-height: 1.1; }
  .contact__title { font-size: 14px; font-weight: 400; line-height: 1.3; }
  .contact__details { margin-top: 20px; font-size: 15px; line-height: 21px; }
</style>
</head>
<body>
<div class="canvas">
  <section class="card card--front"></section>
  <div class="brand">
    <svg class="brand__ring" viewBox="0 0 100 100" aria-hidden="true">
      <circle cx="50" cy="50" r="46" fill="none" stroke="var(--grey)" stroke-width="6"/>
    </svg>
    <span class="brand__name">Ridgeline Outfitters</span>
  </div>

  <section class="card card--back"></section>
  <div class="emblem">
    <svg viewBox="0 0 156 156" aria-hidden="true">
      <circle cx="78" cy="78" r="74" fill="none" stroke="var(--grey)" stroke-width="7"/>
    </svg>
    <span class="emblem__name">Ridgeline<br>Outfitters</span>
  </div>
  <div class="divider"></div>
  <div class="contact">
    <p class="contact__name">Milo Brandt</p>
    <p class="contact__title">Owner</p>
    <div class="contact__details">
      <p>T: 612-555-0187</p>
      <p>www.ridgelineoutfittersmn.example</p>
    </div>
  </div>
</div>
</body>
</html>
```